New Corporate Business Card - Velmorabelle

What we need:
We need a new corporate business card.
We want a new template that we can change by ourself.
We want business card modern and minimalist but that looks professional.
We will print it in 300 gr soft-touch.
Why not a white side with the logo and a red/grey side with the content?
Why not a grey side and a red side like our logo?
I am sure that you have better idea than ours that's the reason we come here.

Who we are:
We are a private label company in cosmetics based in Switzerland. We work in BtoB. We make skin care products for other brands.

Target Market(s)

B to B - Worldwide - any gender

Industry/Entity Type

Cosmetics

Contact Information for Business Card

Side 1:
Logo
Your Swiss Private Label Manufacturer or www.velmorabelle.ch

Side 2:
Name and surname (Example: Lucien Marchetaz)
Job Description (General Manager)
Telephone (+41 32 918 64 00)
Direct (+41 32 918 64 64)
Email (lucien.marchetaz@velmorabelle.ch)
Chemin des Prés-Fleuris 14, 2000 Neuchâtel, Switzerland
www.velmorabelle.ch

Font styles to use
Serif
Sans Serif

Requirements
Must have
• You can use 4 colors: white, red, grey and/or black .
Should not have
• Too much colors, too much things. We want it simple!

```html
<!DOCTYPE html>
<html lang="en">
<head>
<meta charset="utf-8">
<title>Velmorabelle – Business Card</title>
<link rel="stylesheet" href="https://fonts.googleapis.com/css2?family=Source+Sans+3:wght@400;600&display=swap">
<style>
  :root {
    --red: #ee2b3b;
    --grey: #a7a8aa;
    --ink: #2b2b2b;
    --white: #ffffff;
    --backdrop: #e6e6e6;
  }
  * { box-sizing: border-box; margin: 0; padding: 0; }
  html, body { width: 1200px; height: 896px; overflow: hidden; }
  body {
    background: var(--backdrop);
    font-family: "Source Sans 3", Arial, sans-serif;
    display: flex;
    flex-direction: column;
    align-items: center;
    justify-content: center;
    gap: 40px;
  }
  .card {
    position: relative;
    width: 620px;
    height: 400px;
    overflow: hidden;
    box-shadow: 0 4px 14px rgba(0,0,0,.18);
  }

  /* Contact side */
  .card--contact { background: var(--white); }
  .contact {
    position: absolute;
    left: 48px;
    top: 70px;
    color: var(--ink);
  }
  .contact__name {
    font-size: 30px;
    font-weight: 600;
    letter-spacing: -0.5px;
    line-height: 1;
    text-transform: uppercase;
  }
  .contact__first { color: var(--red); }
  .contact__last { color: var(--grey); }
  .contact__role { font-size: 18px; margin: 2px 0 14px; }
  .contact__list { list-style: none; font-size: 15.5px; line-height: 21px; }
  .contact__list li { display: flex; align-items: center; gap: 8px; }
  .contact__list svg { width: 13px; height: 13px; flex: none; fill: var(--red); }

  .brand {
    position: absolute;
    display: flex;
    align-items: center;
    gap: 12px;
    font-weight: 400;
    letter-spacing: 2px;
  }
  .brand__square { width: 18px; height: 18px; flex: none; }
  .card--contact .brand { right: 44px; top: 130px; font-size: 28px; color: var(--red); }
  .card--contact .brand__square { background: var(--grey); }

  .address {
    position: absolute;
    right: 40px;
    bottom: 38px;
    text-align: right;
    font-size: 17px;
    line-height: 21px;
    color: var(--ink);
  }
  .base-band {
    position: absolute;
    left: 0; right: 0; bottom: 0;
    height: 16px;
    display: flex;
  }
  .base-band__red { width: 48%; background: var(--red); }
  .base-band__grey { flex: 1; background: var(--grey); }

  /* Logo side */
  .card--logo { background: var(--grey); }
  .card--logo .field-red {
    position: absolute; left: 0; right: 0; top: 0; height: 50%;
    background: var(--red);
  }
  .card--logo .brand {
    left: 0; right: 0; top: 160px;
    justify-content: center;
    font-size: 44px;
    color: var(--white);
    letter-spacing: 6px;
  }
  .card--logo .brand__square { width: 24px; height: 24px; background: var(--white); }
  .card--logo .site {
    position: absolute; left: 0; right: 0; bottom: 44px;
    text-align: center;
    color: var(--white);
    font-size: 18px;
    letter-spacing: .5px;
  }
</style>
</head>
<body>

<section class="card card--contact" aria-label="Business card, contact side">
  <div class="contact">
    <p class="contact__name"><span class="contact__first">Lucien</span> <span class="contact__last">Marchetaz</span></p>
    <p class="contact__role">General Manager</p>
    <ul class="contact__list">
      <li><svg viewBox="0 0 16 16" aria-hidden="true"><path d="M1 5c0-2 3-3 7-3s7 1 7 3v1h-4V5H5v1H1zM3 7h10l1 7H2z"/></svg>+41 32 918 64 00</li>
      <li><svg viewBox="0 0 16 16" aria-hidden="true"><path d="M1 5c0-2 3-3 7-3s7 1 7 3v1h-4V5H5v1H1zM3 7h10l1 7H2z"/></svg>+41 32 918 64 64 (DIRECT)</li>
      <li><svg viewBox="0 0 16 16" aria-hidden="true"><path d="M1 3h14v10H1zM2 4l6 5 6-5v1L8 10 2 5z" fill-rule="evenodd"/></svg>lucien.marchetaz@velmorabelle.ch</li>
      <li><svg viewBox="0 0 16 16" aria-hidden="true"><circle cx="8" cy="8" r="7"/></svg>www.velmorabelle.ch</li>
    </ul>
  </div>
  <div class="brand"><span class="brand__square"></span>Velmorabelle</div>
  <p class="address">Chemin des Prés-Fleuris 14<br>2000 Neuchâtel, Switzerland</p>
  <div class="base-band"><span class="base-band__red"></span><span class="base-band__grey"></span></div>
</section>

<section class="card card--logo" aria-label="Business card, logo side">
  <div class="field-red"></div>
  <div class="brand"><span class="brand__square"></span>Velmorabelle</div>
  <p class="site">www.velmorabelle.ch</p>
</section>

</body>
</html>
```